Business card design needed

I need a business card design for a new online retail business based in Australia. I am unsure of the exact content of what I will be selling but it will be probably women's clothing, accessories, gym wear, gifts and maybe homeware linen. I am wanting a classy design that portrays the image of class/style/upmarket.

Target Market(s)

predominantely women - 20-50 age group

Industry/Entity Type

Retail

Contact Information for Business Card

Purely Radiant
Harriet Quenby
Director
ABN 73214508836
17 Parrish Lane Kelvin Ridge NSW 2291
ph: +61 417 935 284
sales@purelyradiant.com.au

Logo Text

I am open for suggestions here

Requirements
Must have
• The design must be both sides of the card

```html
<!DOCTYPE html>
<html lang="en">
<head>
<meta charset="UTF-8">
<title>Purely Radiant — Business Card</title>
<link rel="stylesheet" href="https://fonts.googleapis.com/css2?family=Arimo:wght@400&display=swap">
<style>
  :root {
    --stage: #6e6e6e;
    --card: #ffffff;
    --purple: #6a45a3;
    --blue: #1d4fa0;
    --arc-grey: #b9b7bc;
    --arc-grey-dark: #9c9aa0;
    --ink: #565656;
    --ink-soft: #4a4a4a;
    --name-blue: #1f4f9f;
  }
  * { box-sizing: border-box; margin: 0; padding: 0; }
  html, body {
    width: 1200px;
    height: 900px;
    overflow: hidden;
    background: var(--stage);
    font-family: "Arimo", Arial, sans-serif;
  }
  .sheet {
    width: 1200px;
    height: 900px;
    display: flex;
    flex-direction: column;
    align-items: center;
    justify-content: center;
    gap: 56px;
  }
  .card {
    position: relative;
    width: 630px;
    height: 360px;
    background: var(--card);
    overflow: hidden;
  }

  /* Front side */
  .card-front .front-shapes {
    position: absolute;
    inset: 0;
    width: 100%;
    height: 100%;
  }
  .front-brand {
    position: absolute;
    left: 0;
    right: 0;
    top: 150px;
    text-align: center;
    font-size: 44px;
    color: var(--ink);
    letter-spacing: 0.5px;
  }

  /* Back side */
  .card-back { display: flex; }
  .back-strip {
    width: 176px;
    height: 100%;
    background: linear-gradient(180deg, var(--purple) 0%, var(--purple) 45%, var(--blue) 100%);
    position: relative;
  }
  .strip-brand {
    position: absolute;
    left: 0;
    right: 0;
    bottom: 40px;
    text-align: center;
    color: #ffffff;
    font-size: 21px;
  }
  .back-details {
    flex: 1;
    position: relative;
    padding: 118px 0 0 34px;
  }
  .holder-name {
    color: var(--name-blue);
    font-size: 23px;
  }
  .holder-role {
    color: var(--ink-soft);
    font-size: 14px;
    margin-top: 6px;
  }
  .holder-address {
    color: var(--ink-soft);
    font-size: 15px;
    line-height: 1.35;
    margin-top: 82px;
  }
  .contact-list {
    list-style: none;
    margin-top: 14px;
    color: var(--ink-soft);
    font-size: 15px;
    line-height: 1.35;
  }
  .contact-list li {
    display: flex;
    align-items: center;
    gap: 8px;
  }
  .contact-icon {
    width: 11px;
    height: 11px;
    flex: none;
  }
</style>
</head>
<body>
<main class="sheet">

  <section class="card card-front" aria-label="Card front">
    <svg class="front-shapes" viewBox="0 0 630 360" aria-hidden="true">
      <defs>
        <linearGradient id="frontBand" x1="0" y1="1" x2="1" y2="0">
          <stop offset="0" stop-color="#1d4fa0"/>
          <stop offset="0.3" stop-color="#6a45a3"/>
          <stop offset="0.7" stop-color="#6a45a3"/>
          <stop offset="1" stop-color="#1d4fa0"/>
        </linearGradient>
      </defs>
      <rect width="630" height="360" fill="url(#frontBand)"/>
      <ellipse cx="318" cy="172" rx="352" ry="248" transform="rotate(-14 318 172)" fill="#b9b7bc"/>
      <ellipse cx="322" cy="168" rx="336" ry="236" transform="rotate(-14 322 168)" fill="#ffffff"/>
    </svg>
    <p class="front-brand">Purely Radiant</p>
  </section>

  <section class="card card-back" aria-label="Card back">
    <div class="back-strip">
      <p class="strip-brand">Purely Radiant</p>
    </div>
    <div class="back-details">
      <h1 class="holder-name">Harriet Quenby</h1>
      <p class="holder-role">Director</p>
      <p class="holder-address">ABN 73214508836 17 Parrish Lane<br>Kelvin Ridge NSW 2291</p>
      <ul class="contact-list">
        <li>
          <svg class="contact-icon" viewBox="0 0 12 12" aria-hidden="true">
            <path d="M2.5 1 L4.5 1 L5.2 3.6 L4 4.6 Q5 6.9 7.4 8 L8.4 6.8 L11 7.5 L11 9.5 Q10.5 11 9 11 Q1 10 1 2.8 Q1 1.3 2.5 1 Z" fill="#1f4f9f"/>
          </svg>
          <span>+61 417 935 284</span>
        </li>
        <li>
          <svg class="contact-icon" viewBox="0 0 12 12" aria-hidden="true">
            <rect x="0.5" y="2" width="11" height="8" fill="#1f4f9f"/>
            <path d="M0.8 2.4 L6 6.6 L11.2 2.4" fill="none" stroke="#ffffff" stroke-width="1"/>
          </svg>
          <span>sales@purelyradiant.com.au</span>
        </li>
      </ul>
    </div>
  </section>

</main>
</body>
</html>
```